Bright Oak Fitness Facility Business Cards

Business Card Design that incorporates the logo and tagline

Target Market(s)

Fitness, People Who Exercise

Contact Information for Business Card

2718 Harrow Creek Bend
Maple Hollow, Florida 32999
Phone: 352-555-Team (8326)
www.brightoakfitness.example
info@brightoakfitness.example

Requirements
Must have
• Logo, Address, Website, email and tagline "Stronger Every Day". Colors should be red/black/grey/white

```html
<!DOCTYPE html>
<html lang="en">
<head>
<meta charset="utf-8">
<title>Bright Oak Fitness Facility – Business Card</title>
<link href="https://fonts.googleapis.com/css2?family=Montserrat:wght@600;700&display=swap" rel="stylesheet">
<style>
  :root {
    --page: #ffffff;
    --card-black: #121212;
    --card-black-soft: #2a2828;
    --band-dark: #5e5e5e;
    --band-mid: #7e7e7e;
    --band-light: #cdcdcd;
    --edge-strip: #cfcfcf;
    --brand-red: #ed1c24;
    --brand-red-deep: #b8141a;
    --fold-red: #8e0f13;
    --tag-grey: #666666;
    --ink-white: #ffffff;
    --mark-grey: #bdbdbd;
  }
  html, body {
    margin: 0;
    padding: 0;
    width: 1200px;
    height: 1000px;
    overflow: hidden;
    background: var(--page);
  }
  .canvas {
    position: relative;
    width: 1200px;
    height: 1000px;
  }
  .business-card {
    position: absolute;
    left: 0;
    top: 0;
  }
  .card-text {
    font-family: "Montserrat", Arial, sans-serif;
    font-weight: 700;
    fill: var(--ink-white);
  }
  .brand-name { font-size: 20px; letter-spacing: 0.3px; }
  .brand-corner { font-size: 12px; fill: var(--mark-grey); letter-spacing: 1px; }
  .tagline { font-size: 9px; letter-spacing: 0.5px; }
  .contact-line { font-size: 13px; }
  .contact-line.upper { letter-spacing: 0.3px; }
  .icon-stroke { fill: none; stroke: var(--ink-white); stroke-width: 2; stroke-linecap: round; stroke-linejoin: round; }
  .icon-fill { fill: var(--ink-white); }
</style>
</head>
<body>
<div class="canvas">
  <svg class="business-card" width="1200" height="1000" viewBox="0 0 1200 1000" xmlns="http://www.w3.org/2000/svg">
    <defs>
      <clipPath id="card-shape">
        <rect x="288" y="321" width="625" height="357" rx="28" ry="28"/>
      </clipPath>
      <linearGradient id="black-face" x1="0" y1="0" x2="1" y2="0">
        <stop offset="0" stop-color="var(--card-black)"/>
        <stop offset="0.5" stop-color="var(--card-black-soft)"/>
        <stop offset="1" stop-color="#050505"/>
      </linearGradient>
      <linearGradient id="left-face" x1="0" y1="0" x2="1" y2="0">
        <stop offset="0" stop-color="#1a1a1a"/>
        <stop offset="1" stop-color="#2b2b2b"/>
      </linearGradient>
      <linearGradient id="ribbon-red" x1="0" y1="0" x2="1" y2="0">
        <stop offset="0" stop-color="var(--brand-red)"/>
        <stop offset="0.6" stop-color="var(--brand-red)"/>
        <stop offset="1" stop-color="var(--brand-red-deep)"/>
      </linearGradient>
    </defs>

    <g class="card-face" clip-path="url(#card-shape)">
      <rect x="288" y="321" width="625" height="357" fill="url(#left-face)"/>
      <path class="band band-dark" d="M432,321 Q360,500 410,678 L913,678 L913,321 Z" fill="var(--band-dark)"/>
      <path class="band band-mid" d="M478,321 Q408,500 440,678 L913,678 L913,321 Z" fill="var(--band-mid)"/>
      <path class="band band-light" d="M545,321 Q460,500 495,678 L913,678 L913,321 Z" fill="var(--band-light)"/>
      <path class="band band-core" d="M655,321 Q470,480 610,678 L913,678 L913,321 Z" fill="url(#black-face)"/>
      <rect class="edge-strip" x="883" y="321" width="30" height="357" fill="var(--edge-strip)"/>
    </g>

    <g class="brand-ribbon">
      <polygon points="560,568 577,568 577,586" fill="var(--fold-red)"/>
      <rect x="287" y="424" width="290" height="144" fill="url(#ribbon-red)"/>
      <text class="card-text brand-name" x="432" y="512" text-anchor="middle">BRIGHT OAK FITNESS</text>
      <rect class="tagline-bar" x="438" y="545" width="139" height="15" fill="var(--tag-grey)"/>
      <text class="card-text tagline" x="507" y="556" text-anchor="middle">STRONGER EVERY DAY</text>
    </g>

    <text class="card-text brand-corner" x="787" y="395" text-anchor="middle">BRIGHT OAK</text>

    <g class="contact-list">
      <text class="card-text contact-line upper" x="836" y="476" text-anchor="end">2718 HARROW CREEK BEND</text>
      <text class="card-text contact-line upper" x="836" y="494" text-anchor="end">MAPLE HOLLOW, FLORIDA 32999</text>
      <text class="card-text contact-line upper" x="836" y="538" text-anchor="end">352-555-TEAM (8326)</text>
      <text class="card-text contact-line" x="836" y="588" text-anchor="end">www.brightoakfitness.example</text>
      <text class="card-text contact-line" x="834" y="640" text-anchor="end">info@brightoakfitness.example</text>
    </g>

    <g class="icon-tab tab-address">
      <polygon points="884,500 903,500 903,512" fill="var(--fold-red)"/>
      <rect x="847" y="461" width="56" height="39" fill="var(--brand-red)"/>
      <path class="icon-fill" d="M861,469 a8,8 0 0 1 8,8 c0,6 -8,15 -8,15 c0,0 -8,-9 -8,-15 a8,8 0 0 1 8,-8 z M861,474 a3,3 0 1 0 0.01,0 z" fill-rule="evenodd"/>
    </g>
    <g class="icon-tab tab-phone">
      <polygon points="884,551 903,551 903,563" fill="var(--fold-red)"/>
      <rect x="847" y="512" width="56" height="39" fill="var(--brand-red)"/>
      <path class="icon-fill" d="M856,521 l5,-1 l3,7 l-3,2 c1,4 4,7 8,9 l2,-3 l7,3 l-1,5 c-11,1 -22,-10 -21,-22 z"/>
    </g>
    <g class="icon-tab tab-web">
      <polygon points="884,601 903,601 903,613" fill="var(--fold-red)"/>
      <rect x="847" y="562" width="56" height="39" fill="var(--brand-red)"/>
      <circle class="icon-stroke" cx="866" cy="582" r="11"/>
      <ellipse class="icon-stroke" cx="866" cy="582" rx="5" ry="11"/>
      <line class="icon-stroke" x1="855" y1="582" x2="877" y2="582"/>
      <line class="icon-stroke" x1="857" y1="576" x2="875" y2="576"/>
      <line class="icon-stroke" x1="857" y1="588" x2="875" y2="588"/>
    </g>
    <g class="icon-tab tab-email">
      <polygon points="884,653 903,653 903,665" fill="var(--fold-red)"/>
      <rect x="847" y="614" width="56" height="39" fill="var(--brand-red)"/>
      <rect class="icon-stroke" x="856" y="625" width="22" height="16" rx="1"/>
      <polyline class="icon-stroke" points="856,626 867,635 878,626"/>
    </g>
  </svg>
</div>
</body>
</html>
```